Modern Business Card for Lanternfield 2018

Our company assumes the best about people. We are creating an online community of entrepreneurs and business leaders who struggle with marketing their business online.

This business card should POP! We recently got a new logo and are launching a new website next month, so our business cards should make a statement that feels:
-Fresh
-Smart
-Trustworthy
-Fun

Target Market(s)

small business owners, entrepreneurs

Industry/Entity Type

Digital Marketing

Contact Information for Business Card

Dimensions: 3.5" x 2"

Font styles to use
Sans Serif

Colors
f37122
ffffff

Requirements
Must have
• We need a business card with a modern, bold design. We will use one side of the card as a lead-generation offer, so text on one side will need to fit up to 140 characters. The business card should stick to our core colors (orange, black, and white).
Nice to have
• We think a vertical "portrait" design could be interesting.
Should not have
• Should not look like a traditional business card. The round icon should stand out from a distance.

```html
<!DOCTYPE html>
<html lang="en">
<head>
<meta charset="utf-8">
<title>Lanternfield Business Card</title>
<link href="https://fonts.googleapis.com/css2?family=Montserrat:wght@600;700&family=Permanent+Marker&family=Fira+Mono:wght@700&family=Roboto:wght@700&family=Kalam:wght@400&family=Open+Sans:wght@600&display=swap" rel="stylesheet">
<style>
  :root {
    --orange: #f37122;
    --orange-deep: #ec5a0a;
    --orange-soft: #f9cfb3;
    --white: #ffffff;
    --ink: #1a1a1a;
    --backdrop: #3a3a3a;
  }
  html, body { margin: 0; padding: 0; overflow: hidden; }
  body { width: 1200px; height: 1200px; background: var(--backdrop); position: relative; }
  .card { position: absolute; top: 149px; width: 480px; height: 840px; overflow: hidden; }
  .card svg.card-art { position: absolute; inset: 0; }
  .card-front { left: 57px; background: var(--orange); }
  .card-back { left: 646px; background: var(--white); }
  .centered { position: absolute; left: 0; width: 100%; text-align: center; }
  .role { top: 356px; font: 700 16px 'Montserrat', sans-serif; color: var(--ink); }
  .person-name { top: 388px; font: 400 46px 'Permanent Marker', sans-serif; color: var(--ink); letter-spacing: 1px; }
  .email { top: 454px; font: 700 21px 'Montserrat', sans-serif; color: var(--ink); }
  .front-brand { top: 524px; display: flex; justify-content: center; align-items: center; gap: 8px;
    font: 700 14px 'Montserrat', sans-serif; color: var(--orange); letter-spacing: 1px; }
  .dot { width: 22px; height: 22px; border-radius: 50%; background: var(--orange); }
  .benefit { position: absolute; left: 108px; font: 600 17px 'Open Sans', sans-serif; color: var(--white); letter-spacing: 2.5px; }
  .offer-text { position: absolute; left: 80px; top: 341px; width: 300px; font: 700 19px/24px 'Fira Mono', monospace; color: var(--orange); }
  .url-pill { position: absolute; left: 43px; top: 462px; width: 418px; height: 66px; border-radius: 33px; background: var(--orange);
    color: var(--white); font: 700 24px/66px 'Roboto', sans-serif; text-align: center; }
  .back-brand { top: 742px; font: 700 38px 'Roboto', sans-serif; color: var(--white); }
  .tagline { top: 786px; font: 400 24px 'Kalam', cursive; color: var(--white); }
</style>
</head>
<body>

<section class="card card-front">
  <svg class="card-art" width="480" height="840" viewBox="0 0 480 840">
    <rect x="16" y="16" width="448" height="808" fill="var(--white)"/>
    <rect x="14" y="14" width="452" height="812" fill="none" stroke="var(--white)" stroke-width="6" stroke-dasharray="4 3"/>
    <circle cx="383" cy="108" r="40" fill="none" stroke="var(--orange-soft)" stroke-width="18" opacity="0.8"/>
    <circle cx="165" cy="850" r="90" fill="none" stroke="var(--orange-soft)" stroke-width="36" opacity="0.9"/>
    <rect x="36" y="43" width="408" height="752" rx="6" fill="none" stroke="var(--orange)" stroke-width="10"/>
  </svg>
  <div class="centered role">STORY MARKETING COACH</div>
  <div class="centered person-name">DANA WHITLOW</div>
  <div class="centered email">dana@lanternfieldnow.com</div>
  <div class="centered front-brand"><span class="dot"></span>LANTERNFIELD</div>
</section>

<section class="card card-back">
  <svg class="card-art" width="480" height="840" viewBox="0 0 480 840">
    <path d="M0 0 H480 V150 Q260 240 0 245 Z" fill="var(--orange)"/>
    <path d="M0 262 Q270 256 480 165" fill="none" stroke="var(--orange)" stroke-width="7"/>
    <circle cx="480" cy="10" r="90" fill="none" stroke="var(--white)" stroke-width="20"/>
    <circle cx="480" cy="10" r="45" fill="var(--white)"/>
    <g fill="var(--orange)" stroke="var(--white)" stroke-width="4">
      <rect x="52" y="49" width="52" height="40" rx="4"/>
      <rect x="104" y="49" width="272" height="40" rx="4"/>
      <rect x="52" y="104" width="52" height="40" rx="4"/>
      <rect x="104" y="104" width="276" height="40" rx="4"/>
      <rect x="52" y="159" width="52" height="40" rx="4"/>
      <rect x="104" y="159" width="276" height="40" rx="4"/>
    </g>
    <g fill="var(--white)">
      <circle cx="78" cy="60" r="5"/><circle cx="68" cy="74" r="4"/><circle cx="88" cy="74" r="4"/>
      <rect x="62" y="79" width="32" height="4" rx="2"/>
      <circle cx="78" cy="120" r="8"/><rect x="68" y="131" width="20" height="6" rx="3"/>
      <circle cx="78" cy="171" r="5"/><circle cx="70" cy="184" r="5"/><circle cx="86" cy="184" r="5"/>
    </g>
    <text x="78" y="124" font-family="Roboto, sans-serif" font-weight="700" font-size="10" fill="var(--orange)" text-anchor="middle">$</text>
    <rect x="52" y="330" width="409" height="100" fill="none" stroke="var(--orange)" stroke-width="5"/>
    <line x1="390" y1="330" x2="390" y2="430" stroke="var(--orange)" stroke-width="5"/>
    <path d="M400 358 H426 V398" fill="none" stroke="var(--orange)" stroke-width="6"/>
    <path d="M413 392 H439 L426 412 Z" fill="var(--orange)"/>
    <path d="M0 652 L480 584 V840 H0 Z" fill="var(--orange-deep)"/>
    <path d="M0 656 L480 588" fill="none" stroke="var(--white)" stroke-width="8" stroke-dasharray="3 4"/>
    <circle cx="241" cy="697" r="36" fill="var(--white)"/>
  </svg>
  <div class="benefit" style="top:57px">REACH MORE PEOPLE</div>
  <div class="benefit" style="top:112px">MAKE MORE MONEY</div>
  <div class="benefit" style="top:167px">CREATE MORE IMPACT</div>
  <div class="offer-text">Get your free Lanternfield Starter Package and our marketing guide today at</div>
  <div class="url-pill">LANTERNFIELDNOW.COM/START</div>
  <div class="centered back-brand">LANTERNFIELD</div>
  <div class="centered tagline">Tell Stories that inspire action</div>
</section>

</body>
</html>
```